Membership Sales Page Web Design

We need a website designed to showcase the benefits of joining our online community of technology procurement professionals.

Our community has been around for a while and it's time for a refresh. Included in the brief is Verson 1.0 of the site. You can see the current version of the site @ brindlehub.com.

As part of the refresh, we've acquired a new primary domain name (brindle.com) and will be rolling out both a free and paid subscription model.

Because of this, there should be a strong call to sign (join now) infused within the site.

We would like to see site designs that are clean, flat and minimalistic in nature. Our membership colors are royal blue, grey, and white.

The final design should communicate networking and professional growth.

I'd be particularly interestedin seeing some flat website designs with a strong call to action. Here are some great examples for inspiration:

https://pivotlyst.com/
https://marrowkit.io/

Target Market(s)

vantage 400 companies

Number of Pages Required

1 page

Font styles to use
Sans Serif

Colors
0293ce
3276b5
ffffff

Requirements
Must have
• clean, minimalistic, fee
strong call to action
showcase our different membership levels
highlight the benefits of membership
Nice to have
• n/a
Should not have
• n/a

```html
<!DOCTYPE html>
<html lang="en">
<head>
<meta charset="utf-8">
<title>BRINDLE — Technology Acquisition Professionals</title>
<link href="https://fonts.googleapis.com/css2?family=Fira+Sans:wght@400;500;600&family=Roboto:wght@400;500&display=swap" rel="stylesheet">
<style>
:root{
  --blue:#2a7fba;
  --royal:#2279b5;
  --red:#f53b30;
  --ink:#2f3338;
  --text:#3d4248;
  --muted:#6d737a;
  --page:#f7f8fa;
  --band:#eef0f3;
  --card:#f8eeee;
  --plan:#d9dfe6;
  --pink:#f3a5a5;
  --sky:#a9cbe3;
  --white:#ffffff;
}
*{box-sizing:border-box;margin:0;padding:0}
html,body{width:1200px;height:2898px;overflow:hidden}
body{position:relative;background:var(--page);font-family:'Roboto',sans-serif;color:var(--text)}
.abs{position:absolute}
a{color:inherit;text-decoration:none}
.heading{font-family:'Fira Sans',sans-serif;font-weight:500;color:var(--ink);font-size:37px;position:absolute}
.mark{position:relative;display:inline-block}
.mark::after{content:"";position:absolute;height:7px;bottom:4px;z-index:-1}
.mark.pink::after{background:var(--pink);left:56px;width:165px}
.mark.sky::after{background:var(--sky)}
.photo{position:absolute;border-radius:4px}

/* header */
.brand{display:flex;align-items:center;gap:8px;font-family:'Fira Sans',sans-serif;font-weight:600;color:var(--royal)}
.brand-square{background:var(--royal)}
.nav{left:427px;top:72px;display:flex;gap:26px;font-size:15px;color:var(--text)}
.nav .active{position:relative}
.nav .active::after{content:"";position:absolute;left:7px;right:7px;bottom:-9px;height:2px;background:var(--royal)}
.member-btn{left:1034px;top:64px;width:120px;height:33px;background:#cfe0ee;color:var(--royal);font-size:15px;display:flex;align-items:center;justify-content:center;border-radius:2px}

/* hero */
.hero-title{left:145px;top:148px;width:520px;font-family:'Fira Sans',sans-serif;font-weight:600;font-size:43px;line-height:50px;color:var(--blue)}
.hero-text{left:146px;top:320px;width:440px;font-size:18px;line-height:28px;color:var(--text)}
.join-label{left:677px;top:148px;width:384px;text-align:center;font-size:13px;letter-spacing:2px;font-weight:500;color:var(--ink)}
.join-form{left:677px;top:174px;width:384px;border:1px solid #d3d7dc;background:var(--white)}
.field{height:51px;border-bottom:1px solid #e1e4e8;padding:0 16px;display:flex;align-items:center;justify-content:space-between;font-size:15px;color:var(--muted)}
.signup{height:50px;background:var(--red);color:var(--white);font-weight:500;font-size:15px;display:flex;align-items:center;justify-content:center;gap:8px}
.terms{left:677px;top:390px;width:384px;text-align:center;font-size:11px;color:var(--muted)}
.terms span{color:var(--royal)}

/* about */
.band{left:0;top:453px;width:1200px;height:193px;background:var(--band)}
.about-text{left:534px;top:487px;width:490px;font-size:13px;line-height:20px;color:var(--ink)}
.about-text em{display:block;margin-top:20px}
.mission-lead{left:147px;top:790px;width:420px;font-size:16px;line-height:24px;font-family:'Fira Sans',sans-serif;color:var(--ink)}
.mission-text{left:147px;top:860px;width:460px;font-size:14px;line-height:23.5px;font-family:'Fira Sans',sans-serif;color:var(--text)}

/* why */
.why-card{width:288px;height:253px;background:var(--card);border-radius:4px;padding:25px 20px;text-align:center}
.why-card h3{font-size:15px;font-weight:500;color:var(--red);margin-bottom:20px}
.why-card p{font-size:15px;line-height:20px;color:var(--text)}
.benefits{left:787px;top:1226px;width:275px;height:253px;background:var(--red);border-radius:60px 0 60px 0;padding:26px 0 0 52px;list-style:none;color:var(--white);font-size:15px}
.benefits li{height:26.7px;display:flex;align-items:center;gap:10px}
.btn-red{background:var(--red);color:var(--white);font-size:15px;display:flex;align-items:center;justify-content:center}

/* plans */
.plan{text-align:center;position:absolute}
.plan h3{font-family:'Fira Sans',sans-serif;font-weight:500;font-size:34px}
.price{font-size:26px;margin-top:46px}
.price small{font-size:15px}
.features{margin-top:40px;font-size:13px;line-height:27px}
.features b{font-weight:500}
.buy{position:absolute;left:50%;transform:translateX(-50%);width:167px;height:40px;display:flex;align-items:center;justify-content:center;font-size:15px;font-weight:500}
.plan.light{background:var(--plan);color:var(--ink)}
.plan.light .buy{background:var(--royal);color:var(--white)}
.plan.featured{background:var(--royal);color:var(--white);box-shadow:0 2px 8px rgba(0,0,0,.25);z-index:2}
.plan.featured .buy{background:var(--white);color:var(--royal)}

/* certification */
.cert{left:148px;top:2248px;width:912px;height:276px;background:var(--red)}
.cert-title{left:248px;top:2284px;font-family:'Fira Sans',sans-serif;font-weight:500;font-size:35px;color:var(--white)}
.cert-text{left:240px;top:2358px;width:420px;text-align:center;font-size:13px;line-height:20px;font-weight:500;color:var(--white)}
.btn-white{background:var(--white);color:var(--red);font-size:15px;display:flex;align-items:center;justify-content:center}

/* footer */
.foot-head{font-size:14px;font-weight:500;color:var(--ink);letter-spacing:.5px}
.links{left:571px;top:2697px;display:grid;grid-template-columns:99px auto;row-gap:8px;font-size:15px;color:var(--text)}
.social{left:979px;top:2697px;display:flex;gap:12px}
.social span{width:20px;height:20px;border:1.5px solid var(--ink);border-radius:50%}
.legal{left:0;width:1200px;text-align:center;font-size:13px;color:var(--text)}
</style>
</head>
<body>

<header>
  <div class="abs brand" style="left:43px;top:48px;font-size:38px">
    <span class="brand-square" style="width:14px;height:14px"></span>BRINDLE
  </div>
  <nav class="abs nav">
    <a class="active">Home</a><a>Events</a><a>Certifications</a><a>Offerings</a><a>Shop</a>
  </nav>
  <a class="abs member-btn">Member area</a>
</header>

<section class="hero">
  <h1 class="abs hero-title">Promoting excellence among acquisition professionals</h1>
  <p class="abs hero-text">Learn from your peers, get answers to your daily questions, thrive in this ever-changing procurement industry.</p>
  <div class="abs join-label">JOIN US</div>
  <form class="abs join-form">
    <div class="field">Name</div>
    <div class="field">E-mail</div>
    <div class="field">Password
      <svg width="22" height="14" viewBox="0 0 22 14"><path d="M1 7C5 1 17 1 21 7C17 13 5 13 1 7Z" fill="none" stroke="#9aa0a6" stroke-width="1.3"/><circle cx="11" cy="7" r="3" fill="none" stroke="#9aa0a6" stroke-width="1.3"/><line x1="3" y1="13" x2="19" y2="1" stroke="#9aa0a6" stroke-width="1.3"/></svg>
    </div>
    <div class="signup">Sign up
      <svg width="7" height="10" viewBox="0 0 7 10"><path d="M1 1l4 4-4 4" fill="none" stroke="#fff" stroke-width="1.5"/></svg>
    </div>
  </form>
  <p class="abs terms">By clicking "Sign up" I agree to our <span>Terms of Service</span>.</p>
</section>

<section class="about">
  <div class="abs band"></div>
  <h2 class="heading" style="left:152px;top:527px;z-index:1"><span class="mark pink">What is BRINDLE?</span></h2>
  <div class="abs about-text">
    BRINDLE is the only association serving the specialized needs of the technology acquisition professional—the person responsible for negotiating and managing contracts with suppliers of technology products and services.
    <em>Learn from your peers, get answers to your daily questions, thrive in this ever-changing procurement industry.</em>
  </div>

  <h2 class="heading" style="left:276px;top:713px;z-index:1"><span class="mark sky" style="">Mission</span></h2>
  <style>.heading .mark.sky::after{left:20px;width:80px}</style>
  <p class="abs mission-lead">Our mission is to promote and support technology procurement professionals.</p>
  <p class="abs mission-text">BRINDLE works diligently to increase the effectiveness, the image and the impact of these professionals as they serve their organizations and constituents. BRINDLE works diligently to increase the effectiveness, the image and the impact of these professionals as they serve their organizations and constituents.</p>

  <div class="photo" role="img" aria-label="Portrait of a smiling professional woman" style="left:615px;top:703px;width:120px;height:130px;background:linear-gradient(160deg,#e4e5e6,#a7a39b)"></div>
  <div class="photo" role="img" aria-label="Portrait of a woman in a white coat" style="left:840px;top:627px;width:147px;height:157px;background:linear-gradient(160deg,#8ea27d,#dfe3e2)"></div>
  <div class="photo" role="img" aria-label="Portrait of an older smiling woman" style="left:701px;top:884px;width:139px;height:149px;background:linear-gradient(160deg,#b59378,#3a2c26)"></div>
  <div class="photo" role="img" aria-label="Portrait of a young man outdoors" style="left:920px;top:850px;width:114px;height:120px;background:linear-gradient(160deg,#c9d6dc,#7d8f9c)"></div>
  <div class="photo" role="img" aria-label="Portrait of a laughing man by a brick wall" style="left:503px;top:978px;width:83px;height:88px;background:linear-gradient(160deg,#8a5e48,#c9b8a6)"></div>
</section>

<section class="why">
  <h2 class="heading" style="left:0;width:1200px;text-align:center;top:1155px;z-index:1"><span class="mark pink" style="">Why join us?</span></h2>
  <style>.why .mark.pink::after{left:80px;width:75px}</style>
  <div class="abs why-card" style="left:147px;top:1226px">
    <h3>Share information and experiences.</h3>
    <p>As a member, you will learn what kind of deals others are doing, obtain information about vendor ploys and practices, stay informed on best and worst deals, keep up with legislative and regulatory issues affecting your job, and much more.</p>
  </div>
  <div class="abs why-card" style="left:460px;top:1226px">
    <h3>Enhance your performance, network.</h3>
    <p>If you’re the person responsible for negotiating and managing contracts with vendors of technology products and services, BRINDLE membership is for you. It will enhance your performance and facilitate your professional growth while you network with others.</p>
  </div>
  <ul class="abs benefits">
    <li><svg width="12" height="12" viewBox="0 0 12 12"><rect x=".7" y="1.7" width="9.6" height="9.6" fill="none" stroke="#fff" stroke-width="1.2"/><path d="M3 6l2.3 2.3L11 1" fill="none" stroke="#fff" stroke-width="1.3"/></svg>Work Smart</li>
    <li><svg width="12" height="12" viewBox="0 0 12 12"><rect x=".7" y="1.7" width="9.6" height="9.6" fill="none" stroke="#fff" stroke-width="1.2"/><path d="M3 6l2.3 2.3L11 1" fill="none" stroke="#fff" stroke-width="1.3"/></svg>Do Better Deals</li>
    <li><svg width="12" height="12" viewBox="0 0 12 12"><rect x=".7" y="1.7" width="9.6" height="9.6" fill="none" stroke="#fff" stroke-width="1.2"/><path d="M3 6l2.3 2.3L11 1" fill="none" stroke="#fff" stroke-width="1.3"/></svg>Gain valuable skills</li>
    <li><svg width="12" height="12" viewBox="0 0 12 12"><rect x=".7" y="1.7" width="9.6" height="9.6" fill="none" stroke="#fff" stroke-width="1.2"/><path d="M3 6l2.3 2.3L11 1" fill="none" stroke="#fff" stroke-width="1.3"/></svg>Advance your career</li>
    <li><svg width="12" height="12" viewBox="0 0 12 12"><rect x=".7" y="1.7" width="9.6" height="9.6" fill="none" stroke="#fff" stroke-width="1.2"/><path d="M3 6l2.3 2.3L11 1" fill="none" stroke="#fff" stroke-width="1.3"/></svg>Counter vendor ploys</li>
    <li><svg width="12" height="12" viewBox="0 0 12 12"><rect x=".7" y="1.7" width="9.6" height="9.6" fill="none" stroke="#fff" stroke-width="1.2"/><path d="M3 6l2.3 2.3L11 1" fill="none" stroke="#fff" stroke-width="1.3"/></svg>Save time and money</li>
    <li><svg width="12" height="12" viewBox="0 0 12 12"><rect x=".7" y="1.7" width="9.6" height="9.6" fill="none" stroke="#fff" stroke-width="1.2"/><path d="M3 6l2.3 2.3L11 1" fill="none" stroke="#fff" stroke-width="1.3"/></svg>Interact with your peers</li>
    <li><svg width="12" height="12" viewBox="0 0 12 12"><rect x=".7" y="1.7" width="9.6" height="9.6" fill="none" stroke="#fff" stroke-width="1.2"/><path d="M3 6l2.3 2.3L11 1" fill="none" stroke="#fff" stroke-width="1.3"/></svg>Share working solutions</li>
  </ul>
  <a class="abs btn-red" style="left:491px;top:1503px;width:226px;height:39px">Join us today</a>
</section>

<section class="membership">
  <h2 class="heading" style="left:147px;top:1633px;z-index:1"><span class="mark sky">Membership</span></h2>
  <style>.membership .mark.sky::after{left:59px;width:94px}</style>

  <div class="plan light" style="left:148px;top:1727px;width:299px;height:384px;padding-top:36px">
    <h3>Free</h3>
    <div class="price">$ 0 <small>/month</small></div>
    <div class="features" style="margin-top:52px"><b>50</b> videos access<br><b>50</b> support from mentor<br><b>50</b> clients data base</div>
    <a class="buy" style="top:310px">Buy now</a>
  </div>
  <div class="plan featured" style="left:447px;top:1714px;width:356px;height:406px;padding-top:48px">
    <h3>Standard</h3>
    <div class="price">$ 50 <small>/month</small></div>
    <div class="features" style="margin-top:32px;font-weight:500">100 videos access<br>100 support from mentor<br>100 clients data base</div>
    <a class="buy" style="top:323px">Buy now</a>
  </div>
  <div class="plan light" style="left:803px;top:1727px;width:257px;height:384px;padding-top:32px">
    <h3>Plus</h3>
    <div class="price">$ 100 <small>/month</small></div>
    <div class="features" style="margin-top:46px"><b>Unlimited</b> videos access<br><b>Unlimited</b> support from mentor<br><b>Unlimited</b> clients data base</div>
    <a class="buy" style="top:310px">Buy now</a>
  </div>
</section>

<section class="certification">
  <div class="abs cert"></div>
  <h2 class="abs cert-title">Get Professionally Certified</h2>
  <p class="abs cert-text">BRINDLE Certification programs are designed to elevate professional standards, enhance individual performance and identify those who demonstrate knowledge essential to the practice of competent technology procurement.</p>
  <a class="abs btn-white" style="left:339px;top:2458px;width:227px;height:40px">Get certified</a>
  <div class="abs" role="img" aria-label="Smiling businesswoman in a grey suit presenting with an open hand" style="left:710px;top:2185px;width:290px;height:339px;background:linear-gradient(180deg,#6f7480,#4d525c);border-radius:140px 140px 0 0"></div>
  <div class="abs" style="left:688px;top:2198px;width:100px;height:100px;border-radius:50%;background:var(--royal);border:4px solid var(--white)"></div>
</section>

<footer>
  <div class="abs brand" style="left:147px;top:2680px;font-size:44px">
    <span class="brand-square" style="width:16px;height:16px"></span>BRINDLE
  </div>
  <div class="abs foot-head" style="left:605px;top:2667px">QUICK LINKS</div>
  <div class="abs links">
    <a>Home</a><a>Certifications</a><a>Events</a><a>Shop</a><a>Offerings</a><a>Member area</a>
  </div>
  <div class="abs foot-head" style="left:979px;top:2667px">FOLLOW US</div>
  <div class="abs social"><span></span><span></span><span></span></div>
  <p class="abs legal" style="top:2818px">© COPYRIGHT 2019 BRINDLE ASSOCIATION OF TECHNOLOGY ACQUISITION PROFESSIONALS</p>
  <p class="abs legal" style="top:2848px">Helping The World Procurement Community Do Better Deals For 45 Years!</p>
  <p class="abs legal" style="top:2878px">USA 555-014-2290</p>
</footer>

</body>
</html>
```